Landlord Handbook for real estate agency clients

We are a boutique Real Estate Agency that specializes in Property Management (Rentals) Located on Sydney's Northern Beaches.

We are putting together a property owners handbook that informs them about being a landlord, setting up their property for rent, local legislation on leasing properties, the services we offer and what makes us a great choice to manage their property.
Ultimately this is designed to answer new landlords FAQs and sell our agency as the best choice for them.

We want this handbook to be simple, clear and styled to match our existing website. wwww.keystonehavenrealty.com.au

We have supplied some images, screen shots of our Landlord Portal service offered. All words and index are provided in the word.doc
The services we want to feature are:
Our Landlord Portal
Our Service Guarantee
Quality Tenant Database
6 Month Property Reports

I would like the brochure to be around 16-20 A4 pages with some of the images provided and/or any other images you would like to add.

An example of a similar owners handbook can be found here: http://www.vexor.com.au/marlow_tebbit_poh/
But I would like something a little more modern and matched to our website design.

I would like a print ready PDF version of document as well as an editable Photoshop copy and AI copy.

Thank you and I look forward t your designs!
Gus.

Target Market(s)

30-65YO Men and women that own investment properties on Sydney's Northern Beaches

Industry/Entity Type

Real Estate

Font styles to use
Serif

Requirements
Must have
• Must use one of the Town house images provided on the front cover to match our website www.keystonehavenrealty.com.au
• Index of details at the start.
• Use one or all of our screen shot images of the Landlord Portal to promote this feature within the landlord portal description in content.
Should not have
• Any images of foreign currency, landscapes or houses. We are based in Sydney Australia on the beach so we want to keep it local and use Australian images, currency, landscapes and houses.

```html
<!DOCTYPE html>
<html lang="en">
<head>
<meta charset="utf-8">
<title>Keystone Haven Realty – Landlord Handbook</title>
<link href="https://fonts.googleapis.com/css2?family=Oswald:wght@400;500&family=Raleway:wght@300;400&family=Roboto:wght@400;500;700&display=swap" rel="stylesheet">
<style>
:root{
  --stage:#ecebe8;
  --paper:#ffffff;
  --teal:#1d8b99;
  --ink:#2b2b2b;
  --muted:#8a8a8a;
  --rule:#cfcfcf;
  --tab:#c4c4c4;
}
*{margin:0;padding:0;box-sizing:border-box}
html,body{width:1200px;height:2514px;overflow:hidden}
body{background:var(--stage);position:relative;font-family:"Roboto",Arial,sans-serif;color:var(--ink)}
.spread{position:absolute;left:40px;width:1133px;background:var(--paper);overflow:hidden;box-shadow:0 4px 14px rgba(0,0,0,.18)}
.photo{position:absolute}

/* cover */
.cover{top:23px;height:802px}
.cover .photo{left:0;top:0;width:1133px;height:751px;
  background:linear-gradient(172deg,#1c8fd2 0%,#48ade0 12%,#6d7f88 24%,#3e4a4c 34%,#57713f 46%,#3f6a2c 58%,#5c7a3e 68%,#4f5a48 80%,#7b7e78 92%,#8f918c 100%)}
.cover .shade-band{position:absolute;left:0;top:530px;width:1133px;height:80px;background:rgba(20,20,20,.45)}
.cover .shade-corner{position:absolute;left:0;top:530px;width:330px;height:221px;background:rgba(20,20,20,.35)}
.brand{position:absolute;left:722px;top:98px;white-space:nowrap;font-family:"Roboto",Arial,sans-serif;font-weight:700;font-size:26px;color:#1b1b1b;letter-spacing:.3px;line-height:1}
.tagline{position:absolute;right:35px;top:604px;text-align:right;font-family:"Raleway",Arial,sans-serif;font-weight:300;font-size:26px;line-height:1.3;color:#fff;letter-spacing:.5px}
.contacts{position:absolute;left:50px;top:548px;font-size:9.5px;line-height:1.35;color:#f1f1f1}
.contacts p{margin-bottom:10px}
.contacts strong{font-weight:500}
.cover-url{position:absolute;left:253px;top:708px;font-size:11px;letter-spacing:3px;color:#e9e9e9}
.cover .foot-tab{position:absolute;left:0;top:751px;width:40px;height:51px;background:var(--teal)}
.cover .foot-url{position:absolute;right:20px;top:770px;font-size:11px;letter-spacing:2px;color:var(--muted)}

/* index spread */
.index{top:850px;height:784px}
.index svg.photo{left:0;top:0}
.spine{position:absolute;left:560px;top:0;width:1px;height:784px;background:var(--rule)}
.page-tab{position:absolute;left:0;bottom:0;width:56px;height:55px;background:var(--tab)}
.index-title{position:absolute;left:824px;top:334px;font-family:"Oswald",Arial,sans-serif;font-weight:400;font-size:15px;color:var(--teal)}
.index-list{position:absolute;left:824px;top:366px;list-style:none;font-size:10px;line-height:15px;color:var(--ink)}

/* content spread */
.content{top:1668px;height:789px}
.content .photo{left:0;top:0;width:560px;height:789px;
  background:linear-gradient(178deg,#2a8bd6 0%,#7dbfe9 10%,#dfe9ef 16%,#9aa4aa 24%,#3f4a4e 34%,#6f7a78 42%,#4b6a3a 54%,#355f28 66%,#5b7f44 78%,#7f9a6c 88%,#8a8f86 100%)}
.content .page-tab{width:52px;height:57px}
.section-title{position:absolute;left:588px;top:32px;font-family:"Oswald",Arial,sans-serif;font-weight:500;font-size:34px;line-height:1.18;color:var(--teal)}
.column{position:absolute;top:338px;width:258px;font-size:9.6px;line-height:12.2px;color:var(--ink);text-align:justify;hyphens:auto}
.col-a{left:588px}
.col-b{left:862px}
.column h3{font-family:"Roboto",Arial,sans-serif;font-weight:500;font-size:11px;line-height:13px;color:var(--teal);text-transform:uppercase;text-align:left;margin:10px 0 2px}
.column h3:first-child{margin-top:0}
.column p{margin-bottom:1px}
</style>
</head>
<body>

<section class="spread cover">
  <div class="photo" role="img" aria-label="Terraced modern townhouses with glass balconies and landscaped gardens under a blue sky"></div>
  <div class="shade-band"></div>
  <div class="shade-corner"></div>
  <div class="brand">KEYSTONE HAVEN REALTY</div>
  <div class="tagline">PROPERTY MANAGEMENT<br>DONE RIGHT!</div>
  <div class="contacts">
    <p><strong>Keystone Haven Realty</strong><br>PO Box 114<br>Harbourvale NSW 2190<br>info@keystonehavenrealty.com.au</p>
    <p><strong>Gus Calloway</strong><br>Director/Property Manager<br>0400 000 123<br>gus@keystonehavenrealty.com.au</p>
    <p><strong>Tomas Arden</strong><br>Arden Build Co, Maintenance<br>and Repairs<br>0400 000 456<br>tomas@ardenbuild.com.au</p>
  </div>
  <div class="cover-url">www.keystonehavenrealty.com.au</div>
  <div class="foot-tab"></div>
  <div class="foot-url">www.keystonehavenrealty.com.au</div>
</section>

<section class="spread index">
  <svg class="photo" width="1133" height="689" viewBox="0 0 1133 689" role="img" aria-label="Beachside waterfront cafe with timber decking and umbrellas beside the harbour">
    <defs>
      <linearGradient id="cafeTones" x1="0" y1="0" x2="0.15" y2="1">
        <stop offset="0" stop-color="#1a6fc2"/>
        <stop offset=".3" stop-color="#4aa0dc"/>
        <stop offset=".42" stop-color="#c9d4da"/>
        <stop offset=".5" stop-color="#5a3f2c"/>
        <stop offset=".62" stop-color="#8a5a32"/>
        <stop offset=".74" stop-color="#a06a3a"/>
        <stop offset=".84" stop-color="#8e8a84"/>
        <stop offset="1" stop-color="#6f6d6a"/>
      </linearGradient>
    </defs>
    <polygon points="0,0 962,0 630,689 0,689" fill="url(#cafeTones)"/>
  </svg>
  <div class="spine"></div>
  <div class="page-tab"></div>
  <h2 class="index-title">Section 1. Common Questions and Details</h2>
  <ul class="index-list">
    <li>Maxamising your property's return</li>
    <li>Marketing your property</li>
    <li>Selecting the best tenant</li>
    <li>Taking a Bond</li>
    <li>How do we collect rent?</li>
    <li>What happens if the tenant does not pay rent on time?</li>
    <li>When do I receive my rent money?</li>
    <li>What do you charge me?</li>
    <li>Bills and rates</li>
    <li>Management Agreements</li>
    <li>Tenancy Agreements</li>
    <li>Renewing a lease</li>
    <li>Breaking of a fixed term lease</li>
    <li>Condition Reports/Inspections</li>
    <li>Landlord Portal</li>
    <li>Repairing and maintaining my property</li>
    <li>Strata By-Laws</li>
    <li>Landlord Insurance</li>
    <li>Smoke Alarms</li>
    <li>Dryers and washing lines</li>
    <li>Loose Fill Asbestos</li>
    <li>Selling my property while its already being rented.</li>
  </ul>
</section>

<section class="spread content">
  <div class="photo" role="img" aria-label="Modern townhouses stepping down a garden hillside with native plants"></div>
  <div class="page-tab"></div>
  <h1 class="section-title">Section 1.<br>Common Questions<br>and Details</h1>
  <div class="column col-a">
    <h3>Maximising your property's return</h3>
    <p>We ensure your property is bringing in the strongest return possible by minimizing risk, using proven marketing strategies and being able to shortlist the most reliable tenants for you to select from.</p>
    <p>We have an incredibly low vacancy rate. Built through a strong pre-screened tenant database to market your property to, quick-to-act property managers and creating tenancy agreements that end in strong rental seasons, making it easier to re-tenant your property if necessary.</p>
    <p>Providing you with the best tenants possible paying the best possible rent and minimizing any potential vacancy at your property.</p>
    <h3>Marketing your property</h3>
    <p>When listing your property we take high quality pictures, advertise on multiple listing sites including ListingHub.com.au, HomeFinder.com.au, our website, our tenant databases, corporate re-locaters and even social media groups. High quality leasing signage is used out the front of the upcoming property.</p>
    <p>We have two openings per week Saturday and Wednesday and each opening goes for 30min (twice as long as our competitors).</p>
    <p>We also ensure we are available to take people through for private viewings</p>
    <h3>Selecting the best tenant</h3>
    <p>So how do we get the best tenant for your property?</p>
    <p>&nbsp;</p>
    <p>After extensive marketing of your property through multiple media formats. We will receive detailed applications from prospective tenants.</p>
    <p>These applicants are then screened, background checked, employment checked and run through the most up to date digital tenancy databases to ensure they are capable of servicing rent and have no black listed tenancy history.</p>
  </div>
  <div class="column col-b">
    <p>We also ensure your quality tenant gets the attention they deserve and reward them for being great. A great tenant is worth their weight in gold and we ensure they want to continue leasing your property.</p>
    <h3>Taking a bond</h3>
    <p>Current regulations stipulate that the bond can be no more than 4 weeks rent based on the initial tenancy agreement. We use the latest technology with the Tenancy Office Rental Bonds Online – which means we can secure and lodge the bond with the Tenancy Office fast – ensuring you can get your tenant in fast and securely.</p>
    <h3>How do we collect rent?</h3>
    <p>All our tenants pay rent through direct bank deposit. We prefer this method for a number of reasons:</p>
    <p>- By law in NSW Tenants must have a fee-free way of paying rent</p>
    <p>- It is the most convenient form of payment and allows tenants to set automatic payments – ensuring rent is paid on time every time.</p>
    <p>- It is a low cost option for all involved – meaning we keep fees low for landlords.</p>
    <h3>What happens if the tenant does not pay rent on time?</h3>
    <p>We have a zero-arrears policy and all tenants sign an agreement with the following protocol:</p>
    <p>- 2-3 Days in arrears – a phone call, SMS and email are sent</p>
    <p>- 5-8 Days in arrears – a letter is sent to the tenant to advise of breach and the Landlord is notified</p>
    <p>- 15 Days in arrears – Non-Payment of Rent Termination Notice with 14days to vacate.</p>
    <p>In order to minimize risk and maximize the potential of your property we must stick to this strict policy.</p>
  </div>
</section>

</body>
</html>
```